Tidewater Bureau for Crop Wellbeing and Harm Reduction Needs a Flyer Design

We need a flyer design template for our research, education, and prevention center housed at a major university called the "Tidewater Bureau for Crop Wellbeing and Harm Reduction (TBCWHR)." We would like to see designs that use the colors blue and white (PMS 286 (Pantone Matching System) with images that reflect farm scenes in the southeast. I've attached the TBCWHR logo, university logo and copy for the flyer. However, we are most interested in a design template that we can use again and again for new and updated information or for future flyers. This has to be a flyer that we can print on regular paper stock or glossy.
Professionals in agriculture professions; agriculture communities
University

```html
<!DOCTYPE html>
<html lang="en">
<head>
<meta charset="utf-8">
<title>Tidewater Bureau for Crop Wellbeing and Harm Reduction – Flyer</title>
<link rel="stylesheet" href="https://fonts.googleapis.com/css2?family=Teko:wght@400&family=Lato:wght@400;700&display=swap">
<style>
  :root {
    --blue: #0a4fa3;
    --blue-deep: #063a80;
    --blue-light: #2268c4;
    --white: #ffffff;
    --ink: #2b2b2b;
    --tab-grey: #e4e4e4;
    --tab-shade: #b9b9b9;
    --tab-fold: #3a3a3a;
  }
  * { margin: 0; padding: 0; box-sizing: border-box; }
  html, body { width: 869px; height: 1200px; overflow: hidden; background: var(--white); }
  .flyer {
    position: relative; width: 869px; height: 1200px;
    background: var(--white); font-family: "Lato", sans-serif; color: var(--ink);
  }
  .masthead {
    position: absolute; left: 0; top: 0; width: 869px; height: 178px;
    background: linear-gradient(180deg, var(--blue-light), var(--blue) 60%, var(--blue-deep));
    display: flex; align-items: center; justify-content: center;
  }
  .masthead h1 {
    font-family: "Teko", sans-serif; font-weight: 400; color: var(--white);
    text-transform: uppercase; text-align: center; font-size: 66px; line-height: 0.92;
    letter-spacing: 1px; padding-top: 10px;
  }
  .hero {
    position: absolute; left: 0; top: 178px; width: 869px; height: 390px;
    background: linear-gradient(180deg, #9cc3ea 0%, #c9dff2 30%, #8a7a5c 48%, #a99a5d 62%, #8c8a3e 100%);
  }
  .tab-band {
    position: absolute; left: 0; top: 567px; width: 869px; height: 36px; background: var(--blue);
  }
  .info-box {
    position: absolute; top: 603px; height: 213px;
    background: linear-gradient(180deg, var(--blue-light), var(--blue-deep));
    box-shadow: 0 3px 6px rgba(0,0,0,.35);
    color: var(--white); font-size: 17.5px; line-height: 1.3; padding: 36px 22px 0 20px;
  }
  .info-box.what { left: 58px; width: 336px; }
  .info-box.who { left: 477px; width: 336px; }
  .tab {
    position: absolute; top: 535px; height: 68px;
    background: linear-gradient(180deg, #f4f4f4, var(--tab-grey) 60%, var(--tab-shade));
    box-shadow: 0 2px 4px rgba(0,0,0,.3);
    display: flex; align-items: center; justify-content: center;
    font-weight: 700; font-size: 34px; color: #333; text-transform: uppercase;
  }
  .tab.what { left: 35px; width: 377px; }
  .tab.who { left: 450px; width: 382px; }
  .tab-fold { position: absolute; top: 603px; width: 0; height: 0; }
  .tab-fold.left-what { left: 35px; border-top: 13px solid var(--tab-fold); border-left: 23px solid transparent; }
  .tab-fold.right-what { left: 394px; border-top: 13px solid var(--tab-fold); border-right: 18px solid transparent; }
  .tab-fold.left-who { left: 450px; border-top: 13px solid var(--tab-fold); border-left: 27px solid transparent; }
  .tab-fold.right-who { left: 813px; border-top: 13px solid var(--tab-fold); border-right: 19px solid transparent; }

  .facts {
    position: absolute; left: 22px; top: 816px; width: 485px; height: 362px;
    background: var(--white); box-shadow: 2px 3px 6px rgba(0,0,0,.25);
  }
  .facts-label {
    position: absolute; left: 0; top: 29px; width: 228px; height: 58px;
    background: var(--blue); color: var(--white); font-size: 30px;
    display: flex; align-items: center; padding-left: 14px;
  }
  .facts ul {
    position: absolute; left: 14px; top: 108px; width: 462px; list-style: none;
    font-size: 16px; line-height: 1.2; color: #222;
  }
  .facts li { position: relative; padding-left: 14px; }
  .facts li::before {
    content: ""; position: absolute; left: 0; top: 6px; width: 8px; height: 8px;
    border-radius: 50%; background: var(--blue);
  }
  .partners {
    position: absolute; left: 496px; top: 822px; width: 327px; height: 258px;
    background: var(--white); box-shadow: 2px 2px 6px rgba(0,0,0,.2);
    display: flex; flex-direction: column; align-items: center; justify-content: space-evenly;
    text-align: center; color: var(--blue);
  }
  .partner-name { font-size: 18px; font-weight: 700; line-height: 1.25; max-width: 260px; }
  .contact {
    position: absolute; left: 516px; top: 1085px; width: 353px; height: 104px;
    background: linear-gradient(180deg, var(--blue-light), var(--blue-deep));
    color: var(--white); padding: 16px 20px 0 28px;
  }
  .contact-row { display: flex; align-items: center; justify-content: space-between; }
  .phone { font-size: 33px; font-weight: 700; }
  .web { font-size: 21px; margin-top: 4px; }
  .base-band {
    position: absolute; left: 0; top: 1178px; width: 869px; height: 22px; background: var(--blue);
  }
</style>
</head>
<body>
<div class="flyer">
  <header class="masthead">
    <h1>Tidewater Bureau for Crop Wellbeing<br>and Harm Reduction</h1>
  </header>

  <div class="hero" role="img" aria-label="Photo of a weathered wooden barn on a grassy hillside under a blue sky"></div>

  <div class="tab-band"></div>

  <section class="info-box what">Research, education and advocacy to prevent work-related illnesses and injuries and to improve the safety and health of agricultural workers and their families in the southeastern United States.</section>
  <section class="info-box who">Family farmers, farm workers, large producers, professionals working in agricultural health &amp; safety, researchers and communities.</section>

  <div class="tab what">What we do</div>
  <div class="tab who">Who we serve</div>
  <span class="tab-fold left-what"></span><span class="tab-fold right-what"></span>
  <span class="tab-fold left-who"></span><span class="tab-fold right-who"></span>

  <section class="facts">
    <div class="facts-label">Did you know</div>
    <ul>
      <li>Agriculture ranks among the most hazardous industries.</li>
      <li>Agricultural injuries and deaths affect individuals, their families, and their communities.</li>
      <li>Many of the more than 250 persons killed each year in farming related incidents include children, youth and older workers.</li>
      <li>The annual estimated cost of agricultural injuries exceeds $4.5 billion.</li>
      <li>1 in 10 workers in agriculture, forestry and commercial fishing is injured seriously enough to require time off.</li>
      <li>Leading causes of death include tractors, machinery, motor vehicles, and electrocution</li>
    </ul>
  </section>

  <aside class="partners">
    <div class="partner-name">Coastal Plains University<br>College of Public Health</div>
    <div class="partner-name">TBCWHR</div>
  </aside>

  <section class="contact">
    <div class="contact-row">
      <span class="phone">555.214.7730</span>
      <svg width="26" height="22" viewBox="0 0 26 22" aria-hidden="true">
        <path d="M2 7 Q13 -1 24 7 L21 10 L18 7 L8 7 L5 10 Z" fill="#fff"/>
        <rect x="6" y="10" width="14" height="10" rx="2" fill="#fff"/>
      </svg>
    </div>
    <div class="contact-row web">
      <span>www.tbcwhr.cpu.edu</span>
      <svg width="20" height="20" viewBox="0 0 20 20" aria-hidden="true" fill="none" stroke="#fff" stroke-width="1.5">
        <circle cx="10" cy="10" r="8"/><ellipse cx="10" cy="10" rx="3.5" ry="8"/><line x1="2" y1="10" x2="18" y2="10"/>
      </svg>
    </div>
  </section>

  <div class="base-band"></div>
</div>
</body>
</html>
```